Business Card & Word Docs from existing Logo

We need a business card with typical information plus layout to include electrical contractors license number, VORLE license and KMT license. We would like a word document layout for a proposal document, opening page with logo and design basic information; proposal to and proposal from and project name and number. Small basic single page letter for general documents. Email signature with logo.

We are an electrical, refrigeration and automation contractor. We work with reducing energy consumption for our customers and complex process solutions in electrical, refrigeration and automation.
Updates

Reason: Final changes/ revisions to designs.

Target Market(s)

Industrial and commercial businesses that require more than your average contractor.

Industry/Entity Type

Electrical

Requirements
Must have
• Propsal document must have a full opening page.

```html
<!DOCTYPE html>
<html lang="en">
<head>
<meta charset="utf-8">
<title>Frostline Contracting – Business Card</title>
<link rel="stylesheet" href="https://fonts.googleapis.com/css2?family=Open+Sans:wght@400;600&family=Roboto+Condensed:wght@400;700&display=swap">
<style>
  :root {
    --stage: #000000;
    --card-white: #ffffff;
    --ink: #111111;
    --ink-soft: #333333;
    --brand-blue: #2ab3e0;
    --brand-green: #3ccb3c;
    --back-blue: #2b93d6;
    --back-green: #22d400;
    --license-text: #ffffff;
  }
  * { margin: 0; padding: 0; box-sizing: border-box; }
  html, body {
    width: 1200px;
    height: 900px;
    overflow: hidden;
    background: var(--stage);
  }
  .canvas {
    position: relative;
    width: 1200px;
    height: 900px;
    background: var(--stage);
  }
  .card {
    position: absolute;
    top: 291px;
    width: 511px;
    height: 318px;
    overflow: hidden;
  }
  .card--front {
    left: 47px;
    background: var(--card-white);
  }
  .card--back {
    left: 641px;
    background: linear-gradient(90deg, var(--back-blue) 0%, #2aa6b4 40%, #25c23a 70%, var(--back-green) 100%);
  }

  /* Front: company name block */
  .brand {
    position: absolute;
    top: 34px;
    right: 30px;
    display: flex;
    align-items: center;
    gap: 10px;
  }
  .brand__dot {
    width: 30px;
    height: 30px;
    border-radius: 50%;
    background: var(--brand-green);
  }
  .brand__name {
    font-family: "Open Sans", sans-serif;
    font-weight: 600;
    font-size: 24px;
    letter-spacing: 0.5px;
    color: var(--brand-blue);
    line-height: 1;
  }

  /* Front: person */
  .person {
    position: absolute;
    top: 136px;
    right: 30px;
    text-align: right;
    font-family: "Open Sans", sans-serif;
    color: var(--ink);
  }
  .person__name {
    font-weight: 600;
    font-size: 20px;
    line-height: 1.1;
  }
  .person__role {
    font-weight: 400;
    font-size: 15px;
    color: var(--ink-soft);
    line-height: 1.2;
  }

  /* Front: contact */
  .contact {
    position: absolute;
    right: 30px;
    bottom: 20px;
    text-align: right;
    font-family: "Roboto Condensed", sans-serif;
    font-size: 13.5px;
    line-height: 16px;
    color: var(--ink);
  }
  .contact__line--strong { font-weight: 700; }
  .contact__line { font-weight: 400; }

  /* Back: licenses */
  .licenses {
    position: absolute;
    top: 238px;
    left: 272px;
    font-family: "Roboto Condensed", sans-serif;
    font-size: 14px;
    line-height: 20px;
    color: var(--license-text);
    border-collapse: collapse;
  }
  .licenses th {
    font-weight: 700;
    text-align: right;
    padding-right: 14px;
  }
  .licenses td {
    font-weight: 400;
    text-align: left;
  }
</style>
</head>
<body>
<main class="canvas">
  <section class="card card--front" aria-label="Business card front">
    <div class="brand">
      <span class="brand__dot"></span>
      <span class="brand__name">FROSTLINE CONTRACTING</span>
    </div>
    <div class="person">
      <p class="person__name">Daniel Reyes</p>
      <p class="person__role">Director</p>
    </div>
    <div class="contact">
      <p class="contact__line">PO Box 5678, Mackay, Queensland, 4740</p>
      <p class="contact__line contact__line--strong">T 07 5550 2184 &nbsp;|&nbsp; F 07 5550 2185 &nbsp;|&nbsp; M 0400 555 917</p>
      <p class="contact__line">daniel@frostline.com.au &nbsp;|&nbsp; www.frostline.com.au</p>
    </div>
  </section>

  <section class="card card--back" aria-label="Business card back">
    <table class="licenses">
      <tr><th>Contractors License</th><td>12345</td></tr>
      <tr><th>VORLE License</th><td>1234567</td></tr>
      <tr><th>KMT License</th><td>12345</td></tr>
    </table>
  </section>
</main>
</body>
</html>
```